project - Kestra Nook

Dear designers, I'm Looking for an appealing new business card design to represent us for our new e-cigarette store: The KestrA Nook. Knowledgeable and friendly staff we aim for superior customer service with a positive atmosphere. Classic feel with modern touch is what we are aiming for . Lime green font and grey back round is the original color scheme but we are flexible and open to suggestions. I added some doodles to show you where my mind is at. address: 4308 87 Ave NW Edmonton, AB (inside the hollin trade hall)web: thekestranook.com email: info@thekestranook.com phone : 587.555.0148 Thanks and am looking forward to seeing your creative , fresh and innovative designs.
Good luck everybody!
Jonas
lime green and charcoal grey please. thanks
Business
The KestrA Nook

```html
<!DOCTYPE html>
<html lang="en">
<head>
<meta charset="utf-8">
<title>The KestrA Nook – Business Card</title>
<link href="https://fonts.googleapis.com/css2?family=Open+Sans:wght@400;700&display=swap" rel="stylesheet">
<style>
  :root {
    --backdrop: #e6e4e0;
    --charcoal: #5a5d5c;
    --charcoal-dark: #464948;
    --lime: #8cc63f;
    --lime-light: #b5dc5a;
    --lime-dark: #6fae2c;
    --paper: #ffffff;
    --paper-shade: #ececec;
    --ink: #3b3d3d;
  }
  * { margin: 0; padding: 0; box-sizing: border-box; }
  html, body { width: 1200px; height: 894px; overflow: hidden; }
  body {
    background: var(--backdrop);
    position: relative;
    font-family: "Open Sans", sans-serif;
  }
  .card {
    position: absolute;
    top: 287px;
    width: 540px;
    height: 320px;
    border-radius: 18px;
    overflow: hidden;
    box-shadow: 0 10px 24px rgba(0,0,0,0.18);
  }
  .card-front {
    left: 50px;
    background: linear-gradient(135deg, var(--charcoal) 0%, var(--charcoal-dark) 100%);
    display: flex;
    align-items: center;
    justify-content: center;
  }
  .brand-name {
    font-family: "Open Sans", sans-serif;
    font-weight: 400;
    white-space: nowrap;
  }
  .card-front .brand-name { font-size: 44px; color: var(--paper); }
  .card-back {
    left: 610px;
    background: linear-gradient(160deg, var(--paper) 40%, var(--paper-shade) 100%);
  }
  .card-back .brand-name {
    position: absolute;
    left: 34px;
    top: 26px;
    font-size: 32px;
    line-height: 40px;
    color: var(--ink);
  }
  .edge-band {
    position: absolute;
    right: 0; top: 0;
    width: 28px; height: 100%;
    background: linear-gradient(180deg, var(--lime-light), var(--lime-dark));
  }
  .name-tab {
    position: absolute;
    left: 0; top: 88px;
    width: 270px; height: 58px;
    padding: 7px 0 0 34px;
    background: linear-gradient(90deg, var(--lime-dark), var(--lime));
    border-radius: 0 29px 29px 0;
    color: var(--paper);
  }
  .person-name { font-weight: 700; font-size: 20px; letter-spacing: 0.5px; line-height: 24px; }
  .person-title { font-size: 11px; letter-spacing: 1.2px; line-height: 16px; }
  .contact-list {
    position: absolute;
    left: 34px; top: 166px;
    list-style: none;
    color: var(--ink);
    font-size: 14px;
    letter-spacing: 0.4px;
  }
  .contact-list li {
    display: flex;
    align-items: flex-start;
    line-height: 18px;
    margin-bottom: 6px;
  }
  .contact-icon { width: 16px; height: 16px; margin: 1px 10px 0 0; flex: none; }
  .contact-icon circle { fill: none; stroke: var(--lime); stroke-width: 1.4; }
  .contact-icon .glyph { fill: none; stroke: var(--lime); stroke-width: 1.3; stroke-linecap: round; stroke-linejoin: round; }
</style>
</head>
<body>
  <section class="card card-front">
    <div class="brand-name">Kestra Nook</div>
  </section>

  <section class="card card-back">
    <div class="brand-name">Kestra Nook</div>
    <div class="name-tab">
      <div class="person-name">MARA ELLISON</div>
      <div class="person-title">GENERAL MANAGER</div>
    </div>
    <ul class="contact-list">
      <li>
        <svg class="contact-icon" viewBox="0 0 16 16"><circle cx="8" cy="8" r="7"/><path class="glyph" d="M5.5 4.5l1.5 0 .6 1.8-.9.7a4.5 4.5 0 0 0 2.3 2.3l.7-.9 1.8.6 0 1.5c-3.5.4-6.4-2.5-6-6z"/></svg>
        587.555.0148
      </li>
      <li>
        <svg class="contact-icon" viewBox="0 0 16 16"><circle cx="8" cy="8" r="7"/><rect class="glyph" x="5.8" y="4" width="4.4" height="8" rx="0.8"/></svg>
        587.555.0149
      </li>
      <li>
        <svg class="contact-icon" viewBox="0 0 16 16"><circle cx="8" cy="8" r="7"/><rect class="glyph" x="4.5" y="5.5" width="7" height="5"/><path class="glyph" d="M4.5 5.5L8 8.3l3.5-2.8"/></svg>
        INFO@THEKESTRANOOK.COM
      </li>
      <li>
        <svg class="contact-icon" viewBox="0 0 16 16"><circle cx="8" cy="8" r="7"/><circle cx="8" cy="8" r="3.8"/><path class="glyph" d="M4.2 8h7.6M8 4.2c-1.6 2.4-1.6 5.2 0 7.6M8 4.2c1.6 2.4 1.6 5.2 0 7.6"/></svg>
        WWW.THEKESTRANOOK.COM
      </li>
      <li>
        <svg class="contact-icon" viewBox="0 0 16 16"><circle cx="8" cy="8" r="7"/><path class="glyph" d="M8 12.2s-3-3-3-5.2a3 3 0 0 1 6 0c0 2.2-3 5.2-3 5.2z"/><circle cx="8" cy="7" r="1"/></svg>
        <span>4308 87 AVE NW,<br>EDMONTON, AB, CANADA</span>
      </li>
    </ul>
    <div class="edge-band"></div>
  </section>
</body>
</html>
```